GLINT GIN BY TIDE LURE CO

We plan to use a rum product from the caribbean country of Belize CA. That will need to be mentioned somewhere on the label. We want to do a more high-line product, an aged dark rum that plays on the shark theme. We want to use a sleek bottle design with a clever label. Or unique label placement. We need something that will pop off the shelf. We want you to have fun with it and see where it goes. We like the idea of sharks circling around the bottle, possibly like an etching on the glass or back printed on the label or a clear label that can feature the sharks in some capacity. (Not a must) "Chum" because it attracts sharks.

The "Glint Gin" needs a FONT that can become synonymous with the word and then the product. Glint Gin is to be the focus and Tide Lure Co is merely the parent company and requires mention.
Ex:
Tide Lure co.'s Glint Gin
produced in Belize, CA
or Glint Gin produced in Belize for
Tide Lure co.

We have a Glint Gin "mascot" or stamp that is a tribal shark drawing that we want used in the designs where ever you feel fit. We like the stamp as it is, but if you have some tweaks we may consider them.
Updates

I have increased first place to $450.00  and 2nd place to$150.00 !!!

 Everything we have gotten has been great just looking for more ideas. Looking for something sharp and sleek for our bottle we are trying to sell a  upscale rum !! We need it for a aged rum & a white rum .. 

  Thank you !! 
  Torvin

Target Market(s)

MALE 25 TO 45

Industry/Entity Type

It Company

Requirements
Must have
• SHARK THEME ...
Should not have
• OLD WORLD LOOK / MAP LOOKING / TRADITIONAL/ CHEAP.
We don't want everything that has already been done, like all the pirate themes. You can hint at any of these elements in a clever understated way. It is rum after all!

```html
<!DOCTYPE html>
<html lang="en">
<head>
<meta charset="utf-8">
<title>Glint Gin — Tide Lure Co. Label</title>
<link rel="stylesheet" href="https://fonts.googleapis.com/css2?family=Lato:wght@300&display=swap">
<style>
  :root {
    --paper: #ffffff;
    --amber: #d27a14;
    --amber-soft: #e0a25a;
  }
  html, body {
    margin: 0;
    padding: 0;
    width: 1200px;
    height: 1000px;
    overflow: hidden;
    background: var(--paper);
  }
  .canvas {
    width: 1200px;
    height: 1000px;
    display: flex;
    align-items: center;
    justify-content: center;
  }
  .label {
    display: flex;
    flex-direction: column;
    font-family: "Lato", sans-serif;
    font-weight: 300;
    color: var(--amber);
  }
  .label__maker {
    margin: 0 0 4px 6px;
    font-size: 27px;
    line-height: 1.2;
    letter-spacing: 0.04em;
  }
  .label__wordmark {
    margin: 0;
    font-size: 130px;
    font-weight: 300;
    line-height: 1;
    letter-spacing: 0;
  }
  .label__origin {
    margin: 10px 0 0;
    align-self: flex-end;
    font-size: 27px;
    line-height: 1.2;
    letter-spacing: 0.03em;
  }
  .label__fine-print {
    margin: 48px 0 0;
    font-size: 8px;
    line-height: 1.2;
    color: var(--amber-soft);
    white-space: nowrap;
    letter-spacing: 0.02em;
  }
</style>
</head>
<body>
  <main class="canvas">
    <section class="label">
      <p class="label__maker">TIDE LURE CO.</p>
      <h1 class="label__wordmark">glint gin</h1>
      <p class="label__origin">PRODUCT OF BELIZE</p>
      <p class="label__fine-print">Imported 40% Alc./vol. (80 proof) | litre Produced and bottled in Belize City, Belize by the Tide Lure Company</p>
    </section>
  </main>
</body>
</html>
```